professional health club Info Flyer

we need a professional health club DL flyer that will provide information regarding our 24/7 health club services to enquiries whilst we are unstaffed. these will be placed outside on main street.

www.vitrova.club

On the reverse side, we want to offer 2 introductory specials;
1. free 7 day trial
2. Membership, classes & personal training introductory month3 personal training sessions and month 24/7 membership and classes for $99.95 (saving of over $159.85)
conditions: valid for new members only

SIZE: DL with double sided

Target Market(s)

professional, male and female of all ages (in particular those 30+)

Industry/Entity Type

Health And Wellness

Colors
33a6d7
abd037
f78f20
ffffff

Requirements
Must have
• - professional allied health feel about flyer with images
• - contact details
• - services provided include 24/7 memberships, classes, special population group training, Exercise physiology, physiotherapy, massage, nutrition, rehabilitation.
• - a catch to get them to contact us
• - our slogan "We are here to improve your quality of life"

```html
<!DOCTYPE html>
<html lang="en">
<head>
<meta charset="utf-8">
<title>Vitrova Health Club – DL Flyer</title>
<link rel="stylesheet" href="https://fonts.googleapis.com/css2?family=Oswald:wght@500;600;700&family=Lato:ital,wght@0,400;0,700;1,700&family=Montserrat:wght@700;800&display=swap">
<style>
  :root {
    --navy: #0f2f82;
    --blue: #33a6d7;
    --green: #7cb82f;
    --green-light: #abd037;
    --orange: #f78f20;
    --orange-deep: #e07b10;
    --white: #ffffff;
    --ink: #1b1b1b;
    --page: #ececec;
  }
  * { box-sizing: border-box; margin: 0; padding: 0; }
  html, body { width: 1200px; height: 1144px; overflow: hidden; }
  body { background: var(--page); position: relative; font-family: "Lato", sans-serif; }

  .flyer {
    position: absolute; top: 57px; width: 498px; height: 1026px;
    background: var(--white); overflow: hidden;
    box-shadow: 0 6px 18px rgba(0,0,0,.18);
  }
  .flyer--front { left: 62px; }
  .flyer--back { left: 637px; }

  .brand { position: absolute; left: 36px; top: 44px; display: flex; align-items: center; gap: 9px; z-index: 2; }
  .brand__dot { width: 36px; height: 36px; border-radius: 50%; background: var(--blue); }
  .brand__name { font-family: "Montserrat", sans-serif; font-weight: 800; font-size: 29px; color: var(--navy); letter-spacing: 1px; }
  .tagline { position: absolute; left: 36px; top: 100px; font: italic 700 13px "Lato", sans-serif; color: var(--navy); z-index: 2; }

  .photo-band { position: absolute; left: 0; width: 100%; background: linear-gradient(90deg, #22348a, #3b55b3 50%, #2a3f9a); }
  .photo-people { position: absolute; background: linear-gradient(180deg, #cfc6c0, #8f8c92 60%, #5d5f6c); }

  .front .photo-band { top: 193px; height: 277px; }
  .front .photo-people { left: 200px; top: 60px; width: 280px; height: 410px; border-radius: 110px 110px 0 0; }

  .hours { position: absolute; left: 30px; top: 262px; color: var(--white); z-index: 2; }
  .hours__big { font: 700 88px/1 "Oswald", sans-serif; }
  .hours__label { font: 600 30px/1 "Oswald", sans-serif; color: var(--orange); margin-top: 4px; }

  .slogan { position: absolute; left: 0; width: 100%; top: 492px; text-align: center; }
  .slogan__line1 { font: 600 62px/1.05 "Oswald", sans-serif; color: var(--orange); }
  .slogan__line2 { font: 800 44px/1.15 "Montserrat", sans-serif; color: var(--green); margin-top: 4px; }
  .slogan__line3 { font: 700 62px/1.05 "Oswald", sans-serif; color: var(--navy); margin-top: 2px; }

  .offer-box {
    position: absolute; left: 50px; width: 413px; border-radius: 16px;
    background: linear-gradient(180deg, #f9a535, var(--orange) 50%, var(--orange-deep));
    box-shadow: 0 8px 10px -6px rgba(0,0,0,.35);
  }
  .tab {
    position: absolute; left: 50%; transform: translateX(-50%);
    background: var(--navy); color: var(--white); text-align: center;
    clip-path: polygon(0 0, 100% 0, 88% 100%, 12% 100%);
  }
  .services { top: 729px; height: 170px; }
  .services__tab { top: -19px; width: 228px; height: 44px; font: 600 22px/44px "Oswald", sans-serif; }
  .services__list {
    position: absolute; top: 42px; left: 36px; right: 20px;
    display: grid; grid-template-columns: 200px 1fr; column-gap: 12px;
    list-style: none; color: var(--white); font: italic 700 15px/1.3 "Lato", sans-serif;
  }
  .services__list li { position: relative; padding-left: 12px; margin-bottom: 6px; }
  .services__list li::before { content: ""; position: absolute; left: 0; top: 7px; width: 5px; height: 5px; border-radius: 50%; background: var(--navy); }

  .call { position: absolute; left: 50px; top: 938px; display: flex; align-items: baseline; gap: 12px; }
  .call__label { font: 500 24px "Oswald", sans-serif; color: var(--orange); letter-spacing: 1px; }
  .call__number { font: 600 33px "Oswald", sans-serif; color: var(--ink); }

  .web-bar {
    position: absolute; left: 0; bottom: 0; width: 100%; height: 38px;
    background: var(--orange); color: var(--white);
    font: 700 15px/38px "Lato", sans-serif; letter-spacing: 7px; text-align: center;
  }

  .back .photo-band { top: 135px; height: 221px; }
  .back .photo-people { left: 150px; top: 52px; width: 330px; height: 352px; border-radius: 150px 150px 30px 30px; background: linear-gradient(180deg, #e9cfb8, #49a7d6 45%, #1f2436 90%); }

  .intro { position: absolute; left: 24px; top: 420px; width: 345px; font: 400 15.5px/1.3 "Lato", sans-serif; color: var(--ink); }
  .intro__price { color: var(--orange); font-weight: 700; font-size: 15px; }
  .intro__price strong { font-size: 17px; }

  .conditions {
    position: absolute; left: 0; top: 524px; width: 100%; height: 46px;
    background: linear-gradient(90deg, var(--green), var(--green-light));
    color: var(--white); font: 500 22px/46px "Oswald", sans-serif; padding-left: 32px;
  }
  .conditions span { font-family: "Lato", sans-serif; font-weight: 700; font-size: 18px; }

  .trial { top: 615px; height: 170px; text-align: center; }
  .trial__tab { top: -22px; width: 226px; height: 26px; }
  .trial__line1 { font: 700 58px/1 "Oswald", sans-serif; color: var(--white); margin-top: 26px; }
  .trial__line2 { font: 800 66px/1 "Montserrat", sans-serif; color: var(--navy); margin-top: 2px; }

  .contact {
    position: absolute; left: 0; top: 839px; width: 100%; height: 133px;
    background: var(--navy); color: var(--white); text-align: center; padding-top: 14px;
    font: 400 15.5px/1.7 "Lato", sans-serif; font-style: normal;
  }
  .contact__name { font: 600 29px/1.2 "Oswald", sans-serif; color: var(--orange); margin-bottom: 4px; }
</style>
</head>
<body>

<section class="flyer flyer--front front">
  <div class="photo-band" role="img" aria-label="Blurred gym interior with training equipment"></div>
  <div class="photo-people" role="img" aria-label="Man and woman in training clothes lifting a dumbbell together"></div>
  <div class="brand"><span class="brand__dot"></span><span class="brand__name">VITROVA</span></div>
  <p class="tagline">Improving your quality of life</p>

  <div class="hours">
    <div class="hours__big">24/7</div>
    <div class="hours__label">MEMBERSHIPS</div>
  </div>

  <h1 class="slogan">
    <div class="slogan__line1">WE ARE HERE TO</div>
    <div class="slogan__line2">IMPROVE YOUR</div>
    <div class="slogan__line3">QUALITY OF LIFE</div>
  </h1>

  <div class="offer-box services">
    <div class="tab services__tab">SERVICES</div>
    <ul class="services__list">
      <li>Classes</li><li>Physiotherapy</li>
      <li>Special population<br>group training</li><li>Massage</li>
      <li>Exercise physiology</li><li>Nutrition</li>
      <li style="grid-column:2">Rehabilitation</li>
    </ul>
  </div>

  <div class="call"><span class="call__label">CALL US NOW</span><span class="call__number">+612 85550192</span></div>
  <div class="web-bar">www.vitrova.club</div>
</section>

<section class="flyer flyer--back back">
  <div class="photo-band" role="img" aria-label="Blurred gym interior with training equipment"></div>
  <div class="photo-people" role="img" aria-label="Woman in blue top seated, stretching to touch her shoe"></div>
  <div class="brand"><span class="brand__dot"></span><span class="brand__name">VITROVA</span></div>
  <p class="tagline">Improving your quality of life</p>

  <p class="intro">Membership, classes &amp; personal training introductory month3 personal training sessions and month 24/7 membership and classes for<br>
    <span class="intro__price"><strong>$99.95</strong> (saving of over $159.85)</span></p>

  <div class="conditions"><span>Conditions:</span> valid for new members only</div>

  <div class="offer-box trial">
    <div class="tab trial__tab"></div>
    <div class="trial__line1">FREE 7 DAY</div>
    <div class="trial__line2">TRIAL</div>
  </div>

  <address class="contact">
    <div class="contact__name">Jordan Whitfield</div>
    27 Harbour Vale Road, Kellmont Sydney NSW 2230<br>
    +612 85550192<br>
    jordan@vitrova.club
  </address>

  <div class="web-bar">www.vitrova.club</div>
</section>

</body>
</html>
```